Design a Website Home Page

I require a new company home page for my website that has a classic, corporate, high tech look that would be SEO for all major search engines (Wexaro, plimvo ect.) The background will be light grey with a fade. I have attached a sample of the home page for your reference.

Style and font would be similar to http://www.korvelt.ca/ca/brand/en.html and I have attached a sample of the required home page. All other pages will have the same style as the home page. Payment of $100.00 will be made to the winner of this contest and have the option to build the rest of the website as a project.

I will also require a list of questions that you will need answered by me so I understand your needs and requirements to complete the project.

See attached file for your ference. Recommendations for the layout and design would be helpful. I would also need to communicate by SKYPE during the project.

Thanks you.

Jo

```html
<!DOCTYPE html>
<html lang="en">
<head>
<meta charset="utf-8">
<title>Website – Home</title>
<link rel="stylesheet" href="https://fonts.googleapis.com/css2?family=PT+Sans:wght@400;700&family=Noto+Sans:wght@400;700&display=swap">
<style>
  :root {
    --header-top: #000000;
    --header-bottom: #2c2c2c;
    --nav-light: #f1f1f1;
    --nav-dark: #d6d6d6;
    --nav-text: #222222;
    --nav-active: #9a1b1b;
    --page-bg: #ffffff;
    --card-bg: #eeeeee;
    --text: #222222;
    --heading: #111111;
    --accent: #8c0f0f;
    --footer-bg: #141414;
    --footer-head: #c9b58a;
    --footer-text: #dddddd;
    --footer-rule: #3a3a3a;
  }
  * { margin: 0; padding: 0; box-sizing: border-box; }
  html, body { width: 1200px; height: 900px; overflow: hidden; }
  body { background: var(--page-bg); font-family: "Noto Sans", sans-serif; color: var(--text); position: relative; }

  .site-header { height: 116px; background: linear-gradient(var(--header-top), var(--header-bottom)); position: relative; }
  .brand { position: absolute; left: 240px; top: 18px; display: flex; align-items: center; gap: 14px; }
  .brand-mark { width: 80px; height: 80px; border-radius: 50%; background: #d8d8d8; }
  .brand-name { font-family: "PT Sans", sans-serif; font-size: 46px; color: #e8e8e8; letter-spacing: 1px; }
  .slogan { position: absolute; right: 254px; top: 90px; font-family: "PT Sans", sans-serif; font-weight: 700; font-size: 11px; color: #f2f2f2; }

  .main-nav { height: 31px; background: linear-gradient(var(--nav-light), var(--nav-dark)); }
  .main-nav ul { list-style: none; display: flex; margin-left: 270px; }
  .main-nav li { width: 124px; line-height: 31px; font-size: 10px; font-weight: 700; color: var(--nav-text); letter-spacing: 0.3px; }
  .main-nav li.active { color: var(--nav-active); }

  .content { width: 720px; margin: 14px auto 0; }
  .hero { display: block; width: 720px; height: 234px; }

  .features { display: flex; gap: 32px; margin-top: 16px; }
  .feature { width: 156px; height: 161px; background: var(--card-bg); border-radius: 6px; padding: 16px 12px 0 12px; position: relative; }
  .feature h3 { font-family: "PT Sans", sans-serif; font-weight: 400; font-size: 14px; color: var(--heading); margin-bottom: 4px; }
  .feature p { width: 134px; font-size: 10.5px; line-height: 16px; text-align: justify; padding-right: 0; }
  .feature p::before { content: ""; float: right; width: 38px; height: 40px; }
  .feature-icon { position: absolute; right: 12px; top: 38px; width: 32px; height: 32px; }

  .intro { margin-top: 30px; }
  .intro h1 { font-family: "PT Sans", sans-serif; font-weight: 400; font-size: 28px; color: var(--heading); }
  .intro p { font-size: 11px; line-height: 16px; margin-top: 6px; }
  .intro a { color: var(--accent); font-weight: 700; text-decoration: none; }

  .columns { display: flex; gap: 30px; margin-top: 36px; }
  .column { width: 345px; }
  .column h2 { font-family: "PT Sans", sans-serif; font-weight: 400; font-size: 14px; color: var(--heading); margin-bottom: 6px; }
  .column p { font-size: 10.5px; line-height: 16px; text-align: justify; }

  .site-footer { position: absolute; left: 0; top: 833px; width: 1200px; height: 67px; background: radial-gradient(ellipse at 40% 0%, #2a2a2a, var(--footer-bg) 60%); }
  .footer-cols { width: 720px; margin: 0 auto; display: flex; gap: 32px; padding-top: 20px; }
  .footer-col { width: 210px; }
  .footer-col h4 { font-family: "PT Sans", sans-serif; font-weight: 400; font-size: 16px; color: var(--footer-head); padding-bottom: 8px; border-bottom: 1px solid var(--footer-rule); }
  .footer-col p { font-size: 10.5px; color: var(--footer-text); margin-top: 8px; }
</style>
</head>
<body>
  <header class="site-header">
    <div class="brand">
      <span class="brand-mark"></span>
      <span class="brand-name">WEBSITE</span>
    </div>
    <div class="slogan">YOUR WEBSITE SLOGAN HERE</div>
  </header>

  <nav class="main-nav">
    <ul>
      <li class="active">HOME</li>
      <li>PRODUCTS</li>
      <li>SERVICES</li>
      <li>NEWS</li>
      <li>ABOUT</li>
    </ul>
  </nav>

  <main class="content">
    <svg class="hero" viewBox="0 0 720 234" role="img" aria-label="Photo of a glass office tower seen from below">
      <defs>
        <linearGradient id="heroFill" x1="0" y1="0" x2="1" y2="1">
          <stop offset="0" stop-color="#c9ccd6"/>
          <stop offset="0.5" stop-color="#9a9a9c"/>
          <stop offset="1" stop-color="#d0d0d0"/>
        </linearGradient>
      </defs>
      <path d="M8 0 H712 Q720 0 720 8 V220 Q360 250 0 218 V8 Q0 0 8 0 Z" fill="url(#heroFill)"/>
    </svg>

    <section class="features">
      <article class="feature">
        <h3>Zepkit on board</h3>
        <svg class="feature-icon" viewBox="0 0 32 32" aria-hidden="true">
          <rect x="2" y="14" width="7" height="16" fill="#3d7bd6"/>
          <rect x="11" y="6" width="7" height="24" fill="#e5862a"/>
          <rect x="20" y="10" width="7" height="20" fill="#4aa843"/>
        </svg>
        <p>Lorem ipsum dolor sit amet, turpis egestas commodo, eget non ultrices nec lectus, ac interdum, netus aliquam.</p>
      </article>
      <article class="feature">
        <h3>Slideshow</h3>
        <svg class="feature-icon" viewBox="0 0 32 32" aria-hidden="true">
          <rect x="5" y="3" width="22" height="27" rx="2" fill="#f3c53a"/>
          <rect x="8" y="6" width="16" height="21" rx="1" fill="#f9dd6e"/>
        </svg>
        <p>Lorem ipsum dolor sit amet, turpis egestas commodo, eget non ultrices nec lectus, ac interdum, netus aliquam.</p>
      </article>
      <article class="feature">
        <h3>Fontlo fonts</h3>
        <svg class="feature-icon" viewBox="0 0 32 32" aria-hidden="true">
          <circle cx="16" cy="16" r="14" fill="#2f7fd0"/>
          <path d="M8 10 Q14 8 16 14 Q14 20 10 22 Q6 16 8 10 Z M18 6 Q26 10 26 18 Q22 16 20 12 Z" fill="#4fae3c"/>
        </svg>
        <p>Lorem ipsum dolor sit amet, turpis egestas commodo, eget non ultrices nec lectus, ac interdum, netus aliquam.</p>
      </article>
      <article class="feature">
        <h3>Tableless</h3>
        <svg class="feature-icon" viewBox="0 0 32 32" aria-hidden="true">
          <circle cx="16" cy="16" r="15" fill="#e86a1c"/>
        </svg>
        <p>Lorem ipsum dolor sit amet, turpis egestas commodo, eget non ultrices nec lectus, ac interdum, netus aliquam.</p>
      </article>
    </section>

    <section class="intro">
      <h1>Heading sample with Fontlo font</h1>
      <p>This template is free. You are free to use it, share it, redistribute it, modify it in any way you want as long as you <strong>keep a link back to veloTemplate Website</strong> in the footer. You can remove this link by making a $10 <a href="#">donation</a>.</p>
    </section>

    <section class="columns">
      <div class="column">
        <h2>Heading 3 sample</h2>
        <p>Lorem ipsum dolor sit amet, turpis egestas commodo, eget non ultrices nec lectus, ac interdum, netus aliquam, vulputate vel reiciendis risus.</p>
      </div>
      <div class="column">
        <h2>Lightweight XHTML / CSS template</h2>
        <p>Lorem ipsum dolor sit amet, turpis egestas commodo, eget non ultrices nec lectus, ac interdum, netus aliquam.</p>
      </div>
    </section>
  </main>

  <footer class="site-footer">
    <div class="footer-cols">
      <div class="footer-col"><h4>Company</h4><p>Who are we</p></div>
      <div class="footer-col"><h4>Products</h4><p>Products</p></div>
      <div class="footer-col"><h4>Blog archives</h4><p>Lorem ipsum</p></div>
    </div>
  </footer>
</body>
</html>
```